"Quiet Lanterns Burning" cat novel book cover

Cover for a novel about a vet tech who saves two kittens from euthanization and ends up entangled in an adventure she never could have dreamed.

Novel has four point-of-view characters: a female vet tech protagonist, a one-eyed kitten who she saves and adopts, a male pastor who befriends the vet tech after finding said kitten hiding under his porch, and a pharmaceutical executive antagonist in charge of a dubious feline weight-loss drug.

The two kittens saved by the protagonist also fall in love about 1/4 of the way through the story. One of them has a CNS condition that makes it hard for them to walk, and the point-of-view cat serves as a protector and defender of the disabled one.

Narrative has a lot of focus on the emotional lives of the characters and their relationships, but it is not a romance novel per se. While the title is a Biblical reference and religion and spirituality are important to some of the characters, it is also not meant to support any particular belief system.

Target Market(s)

Cat lovers

Requirements
Must have
• Title: Quiet Lanterns Burning
Author: Delia Brackenford
Tagline (to appear on cover): Even the smallest kitty can change the world
Nice to have
• I originally intended to use the attached photo representing the story's central kittens. I was going to apply some filters to make it look hand-drawn and disguise the low resolution. I quickly realized my graphic design skills are not sufficient to make that look professional, which led me here. If you can make it work with that photo, it would be lovely; if not, I am totally open to alternative concepts.
Should not have
• The appearances and even the ages of the characters are not solidified in the text, in order to allow the reader to imagine them any way they prefer. So I would prefer avoiding any specific visual representations of them, outside of something vague like a silhouette.

```html
<!DOCTYPE html>
<html lang="en">
<head>
<meta charset="utf-8">
<title>Quiet Lanterns Burning — Book Cover</title>
<link href="https://fonts.googleapis.com/css2?family=Bodoni+Moda:opsz,wght@6..96,500&family=Open+Sans:wght@400;500&display=swap" rel="stylesheet">
<style>
  :root {
    --peach-top: #fbd393;
    --peach-mid: #fbc98f;
    --coral-low: #f8a184;
    --author-band: #f68a72;
    --ink: #111111;
    --photo-dark: #3a3426;
    --photo-mid: #8a7a5c;
    --photo-light: #efe6d2;
  }
  html, body {
    margin: 0;
    padding: 0;
    width: 840px;
    height: 1200px;
    overflow: hidden;
  }
  .cover {
    position: relative;
    width: 840px;
    height: 1200px;
    background: linear-gradient(to bottom, var(--peach-top) 0%, var(--peach-mid) 70%, var(--coral-low) 100%);
    overflow: hidden;
  }
  .tagline {
    position: absolute;
    top: 24px;
    left: 0;
    width: 100%;
    text-align: center;
    font-family: "Open Sans", Arial, sans-serif;
    font-size: 17px;
    letter-spacing: 0.5px;
    color: var(--ink);
    margin: 0;
  }
  .title {
    position: absolute;
    top: 96px;
    left: 0;
    width: 100%;
    text-align: center;
    font-family: "Bodoni Moda", "Playfair Display", serif;
    font-weight: 500;
    font-size: 72px;
    line-height: 82px;
    color: var(--ink);
    margin: 0;
    text-transform: uppercase;
  }
  .kittens-photo {
    position: absolute;
    left: 10px;
    top: 285px;
    width: 810px;
    height: 845px;
  }
  .author-band {
    position: absolute;
    left: 0;
    bottom: 0;
    width: 100%;
    height: 68px;
    background: var(--author-band);
    display: flex;
    align-items: center;
    justify-content: center;
  }
  .author {
    font-family: "Open Sans", Arial, sans-serif;
    font-weight: 500;
    font-size: 31px;
    letter-spacing: 1px;
    color: var(--ink);
    text-transform: uppercase;
    margin: 0;
  }
</style>
</head>
<body>
  <div class="cover">
    <p class="tagline">EVEN THE SMALLEST KITTY CAN CHANGE THE WORLD</p>
    <h1 class="title">Quiet Lanterns<br>Burning</h1>

    <svg class="kittens-photo" viewBox="0 0 810 845" role="img" aria-label="Photo of two kittens curled up together, a dark tabby and a white and tan cat, in an oval vignette">
      <defs>
        <radialGradient id="photo-tone" cx="55%" cy="40%" r="65%">
          <stop offset="0%" stop-color="var(--photo-mid)"/>
          <stop offset="55%" stop-color="var(--photo-dark)"/>
          <stop offset="100%" stop-color="var(--photo-light)"/>
        </radialGradient>
        <radialGradient id="light-patch" cx="25%" cy="78%" r="35%">
          <stop offset="0%" stop-color="var(--photo-light)" stop-opacity="0.95"/>
          <stop offset="100%" stop-color="var(--photo-light)" stop-opacity="0"/>
        </radialGradient>
      </defs>
      <ellipse cx="415" cy="430" rx="395" ry="415" fill="url(#photo-tone)"/>
      <ellipse cx="415" cy="430" rx="395" ry="415" fill="url(#light-patch)"/>
    </svg>

    <div class="author-band">
      <p class="author">Delia Brackenford</p>
    </div>
  </div>
</body>
</html>
```